Solution Matrix for our Company

Develop an image that describes our "4 solutions". We eventually will list the products and services we have that address the solution being discussed. Our main website is http://brightlane4jobs.example/. Feel free to look through the material there as well as the material we are addressing.

The mock document is a summary of the 4 solution buckets. We have also attached some samples from states that have done similar work. Feel free to be creative and use graphics and/or pictures in your design

Target Market(s)

Education

```html
<!DOCTYPE html>
<html lang="en">
<head>
<meta charset="utf-8">
<title>Brightlane Learning – Solution Matrix</title>
<link rel="stylesheet" href="https://fonts.googleapis.com/css2?family=Arimo:wght@400;700&display=swap">
<style>
  :root{
    --page:#ffffff;
    --cream:#fbf7ec;
    --panel:#f2eee2;
    --ink:#58595b;
    --orange:#f7941d;
    --figure-light:#e1e2e6;
    --figure-mid:#c9c9cc;
  }
  *{box-sizing:border-box;margin:0;padding:0}
  html,body{width:1200px;height:1124px;overflow:hidden;background:var(--page)}
  body{font-family:"Arimo",Arial,sans-serif;color:var(--ink);position:relative}
  .sheet{position:absolute;left:50px;top:19px;width:1100px;height:1086px;background:var(--cream)}
  .intro-panel{position:absolute;left:62px;top:59px;width:1076px;height:235px;background:var(--panel)}
  .brand-name{position:absolute;left:71px;top:118px;display:flex;align-items:center;gap:12px;
    font-weight:700;font-size:54px;line-height:1;color:var(--orange)}
  .brand-square{width:16px;height:16px;background:var(--orange)}
  .mission{position:absolute;left:71px;top:216px;width:480px;font-size:14.6px;line-height:18.5px;color:var(--orange)}
  .matrix-panel{position:absolute;left:62px;top:345px;width:1076px;height:699px;background:var(--panel)}
  .student-art{position:absolute;left:412px;top:414px;width:378px;height:462px;border-radius:46% 46% 8% 8%;
    background:linear-gradient(160deg,var(--figure-light) 0%,var(--figure-mid) 55%,var(--orange) 100%);opacity:.85}
  .connectors{position:absolute;left:0;top:0;width:1200px;height:1124px}
  .solution{position:absolute;font-size:17.2px;line-height:21.1px;hyphens:auto;-webkit-hyphens:auto}
  .solution h2{font-size:17.2px;font-weight:700;line-height:21.1px}
  .solution ul{list-style:none}
  .solution li{color:var(--orange)}
  .solution li::before{content:"•";display:inline-block;width:27px}
  .solution--supported{left:71px;top:359px;width:286px}
  .solution--prepared{left:847px;top:356px;width:288px}
  .solution--engaged{left:71px;top:826px;width:286px}
  .solution--wise{left:853px;top:825px;width:284px}
  .footer-name{position:absolute;right:63px;top:1071px;text-align:right;white-space:nowrap}
  .footer-name strong{display:block;font-size:16px;font-weight:700;color:var(--orange);line-height:17px}
  .footer-name span{display:block;font-size:8px;letter-spacing:.6px;color:var(--ink);line-height:10px}
</style>
</head>
<body>
  <div class="sheet"></div>
  <section class="intro-panel"></section>
  <div class="brand-name"><span class="brand-square"></span><span>Brightlane</span></div>
  <p class="mission">Brightlane Learning relies on robust labor market data tools and sound educational research to guide our development efforts and encourage the use of informed career readiness practices educational settings.</p>

  <section class="matrix-panel"></section>
  <div class="student-art" role="img" aria-label="Illustration of a student sitting cross-legged on a stack of books, reading and thinking"></div>

  <svg class="connectors" viewBox="0 0 1200 1124" aria-hidden="true">
    <g stroke="#f7941d" stroke-width="2" stroke-dasharray="7 5" fill="none">
      <line x1="374" y1="434" x2="488" y2="499"/>
      <line x1="826" y1="376" x2="738" y2="416"/>
      <line x1="247" y1="813" x2="396" y2="726"/>
      <line x1="840" y1="825" x2="780" y2="778"/>
    </g>
    <g fill="#f7941d">
      <circle cx="374" cy="434" r="5.5"/>
      <circle cx="826" cy="376" r="4"/>
      <circle cx="247" cy="813" r="7"/>
      <circle cx="840" cy="825" r="3"/>
    </g>
  </svg>

  <article class="solution solution--supported">
    <h2>Career Supported</h2>
    <p>Students benefit from informed educational leadership and policymaking that result in effective career resources and learning opportunities.</p>
    <ul>
      <li>Brightlane Policy Tools</li>
      <li>Carver IV Technical Support</li>
      <li>Professional Development</li>
      <li>Industry-Education Relationships</li>
    </ul>
  </article>

  <article class="solution solution--prepared">
    <h2>Career Prepared</h2>
    <p>Students have the necessary foundational, technical, and workplace skills needed to support success in a variety of careers.</p>
    <ul>
      <li>Career-Focused Curricula</li>
      <li>Math Assessments with Scalewise Career Database (powered by the Scalewise® Framework for Mathematics)</li>
    </ul>
  </article>

  <article class="solution solution--engaged">
    <h2>Career Engaged</h2>
    <p>Students are motivated and inspired to develop career skills and seek employment opportunities that meet both personal and community needs.</p>
    <ul>
      <li>Career Awareness &amp; Exposure</li>
      <li>Purposeful Learning Connected to Careers</li>
    </ul>
  </article>

  <article class="solution solution--wise">
    <h2>Career Wise</h2>
    <p>Students have insight into personal values and interests, as well as the economic realities of the job market, that supports informed career decisions</p>
    <ul>
      <li>Career Pathways</li>
      <li>Career Exploration</li>
      <li>Educator Career Guides</li>
    </ul>
  </article>

  <div class="footer-name"><strong>BRIGHTLANE LEARNING</strong><span>Guiding Every Learner Forward</span></div>
</body>
</html>
```